Need 4 childhood cancer facts posters

Hello. I run a nonprofit in East Tennessee, USA that supports children with cancer and their families.

I need 4 poster designs with facts about childhood cancers. It should either have pictures of children with cancer or be focused around the whole idea of childhood cancer awareness. This project will require time and research. I will post links to facts as the project goes forward.

Questions can be emailed to tmerrow@glowwithnora.org. AI format of our logo has been uploaded. I have images and links here http://www.glowwithnora.org/contest-pics.html

You can also view our website at www.glowwithnora.org

Some facts: http://pelt.tumorstats.example/archive/publications/childhood/

USE THESE FACTS: * Everyday, approximately 250 children will die from childhood cancer. *Childhood Cancers is the number 1 cause of death in children under age 15 in the US. *Less than 5% of the federal governments budget toward cancer research is dedicated to childhood cancers. *One in 330 children will be diagnosed with cancer by the time they are 20.

Poster will be 24 inches wide by 36 inches tall.

```html
<!DOCTYPE html>
<html lang="en">
<head>
<meta charset="utf-8">
<title>Childhood Cancer Facts Posters</title>
<link href="https://fonts.googleapis.com/css2?family=Courier+Prime&family=Josefin+Sans:wght@400&display=swap" rel="stylesheet">
<style>
  :root {
    --board: #4a5757;
    --crimson: #a3062f;
    --lime: #6bd400;
    --mint: #72d4ad;
    --tangerine: #e8821a;
    --ink-light: #ffffff;
    --ink-dark: #2b2b2b;
    --ribbon: #f5e100;
  }
  * { box-sizing: border-box; margin: 0; padding: 0; }
  html, body {
    width: 1010px;
    height: 1200px;
    overflow: hidden;
    background: var(--board);
  }
  .board {
    position: relative;
    width: 1010px;
    height: 1200px;
  }
  .poster {
    position: absolute;
    width: 233px;
    height: 360px;
    overflow: hidden;
  }
  .poster--daily     { left: 136px; top: 120px; background: var(--crimson); }
  .poster--leading   { left: 641px; top: 120px; background: var(--lime); }
  .poster--funding   { left: 136px; top: 719px; background: var(--mint); }
  .poster--odds      { left: 641px; top: 719px; background: var(--tangerine); }

  .poster__photo {
    position: absolute;
    left: 0; top: 0;
    width: 100%;
    height: 156px;
    clip-path: polygon(0 0, 100% 0, 100% 104px, 0 156px);
  }
  .poster--daily .poster__photo   { background: radial-gradient(circle at 40% 50%, #e7c4b0 0 22%, transparent 40%), linear-gradient(120deg, #c56a6a, #d99a94 55%, #b75a5a); }
  .poster--leading .poster__photo { background: radial-gradient(circle at 32% 45%, #f0d2c0 0 24%, transparent 42%), linear-gradient(160deg, #8fd24a, #4fa321); }
  .poster--funding .poster__photo { background: radial-gradient(circle at 48% 45%, #f3ddd2 0 22%, transparent 40%), linear-gradient(180deg, #eef4f7, #b8ccd6); }
  .poster--odds .poster__photo    { background: radial-gradient(circle at 55% 45%, #b7876a 0 20%, transparent 40%), linear-gradient(180deg, #c9cbcd, #a9acae); }

  .poster__message {
    position: absolute;
    left: 18px; right: 19px; top: 190px;
    display: flex;
    flex-direction: column;
  }
  .poster__fact {
    font-family: "Courier Prime", monospace;
    font-size: 9.4px;
    letter-spacing: -0.3px;
    line-height: 12.8px;
    text-align: center;
    color: var(--ink-light);
  }
  .poster__tagline {
    align-self: flex-end;
    margin-top: 30px;
    font-family: "Josefin Sans", sans-serif;
    font-size: 6.8px;
    letter-spacing: 0.1px;
    color: var(--ink-light);
    white-space: nowrap;
  }
  .poster__tagline b { font-weight: 400; font-size: 9px; margin-right: 2px; }

  .poster__url {
    position: absolute;
    left: 17px; top: 324px;
    font-family: "Josefin Sans", sans-serif;
    font-size: 6px;
    color: var(--ribbon);
  }
  .poster__org {
    position: absolute;
    right: 17px; top: 314px;
    display: flex;
    align-items: center;
    gap: 4px;
    font-family: "Courier Prime", monospace;
    color: var(--ink-dark);
  }
  .poster__org-dot {
    width: 8px; height: 8px;
    border-radius: 50%;
    background: var(--ribbon);
  }
  .poster__org-name {
    font-size: 6.5px;
    line-height: 7.5px;
    text-align: center;
    letter-spacing: 0.4px;
  }
</style>
</head>
<body>
<main class="board">

  <article class="poster poster--daily">
    <div class="poster__photo" role="img" aria-label="Smiling girl in a pink floral headscarf against a soft red background"></div>
    <div class="poster__message">
      <p class="poster__fact">Every day, approximately 250 children will die from childhood cancer.</p>
      <p class="poster__tagline"><b>...</b> LET'S MAKE THEIR TOUGH ROAD EASIER</p>
    </div>
    <p class="poster__url">glowwithnora.org</p>
    <div class="poster__org"><span class="poster__org-dot"></span><span class="poster__org-name">Nora Merrow<br>CHILDHOOD CANCER<br>FOUNDATION</span></div>
  </article>

  <article class="poster poster--leading">
    <div class="poster__photo" role="img" aria-label="Smiling boy with a nasal tube standing on green grass"></div>
    <div class="poster__message">
      <p class="poster__fact">Childhood cancer is the number 1 cause of death in children under age 15 in the US.</p>
      <p class="poster__tagline"><b>...</b> LET'S MAKE THEIR TOUGH ROAD EASIER</p>
    </div>
    <p class="poster__url">glowwithnora.org</p>
    <div class="poster__org"><span class="poster__org-dot"></span><span class="poster__org-name">Nora Merrow<br>CHILDHOOD CANCER<br>FOUNDATION</span></div>
  </article>

  <article class="poster poster--funding">
    <div class="poster__photo" role="img" aria-label="Girl in a mint headscarf holding a plush toy by the water"></div>
    <div class="poster__message">
      <p class="poster__fact">Less than 5% of the federal government's budget toward cancer research is dedicated to childhood cancers.</p>
      <p class="poster__tagline"><b>...</b> LET'S MAKE THEIR TOUGH ROAD EASIER</p>
    </div>
    <p class="poster__url">glowwithnora.org</p>
    <div class="poster__org"><span class="poster__org-dot"></span><span class="poster__org-name">Nora Merrow<br>CHILDHOOD CANCER<br>FOUNDATION</span></div>
  </article>

  <article class="poster poster--odds">
    <div class="poster__photo" role="img" aria-label="Boy in a hospital gown flexing his arm with an IV line, on grey"></div>
    <div class="poster__message">
      <p class="poster__fact">One in 330 children will be diagnosed with cancer by the time they are 20.</p>
      <p class="poster__tagline"><b>...</b> LET'S MAKE THEIR TOUGH ROAD EASIER</p>
    </div>
    <p class="poster__url">glowwithnora.org</p>
    <div class="poster__org"><span class="poster__org-dot"></span><span class="poster__org-name">Nora Merrow<br>CHILDHOOD CANCER<br>FOUNDATION</span></div>
  </article>

</main>
</body>
</html>
```